Professional/modern business card design for construction company

We need a new business card design, double sided keeping it modern, sleek, professional and simple. We are an earthmoving business but do not want any pictures of machinery. I would like one side to have the logo and the other to have all the information, keeping with the colors in our logo. The business card will need to be able to be customised so we can use it for several different managers., we would also like to be able to use the design to apply it to other stationary ie. letterheads, notebooks etc. We do not really have a tag line but we could put on there that we specialise in - Agriculture, Civil Construction and Mining.

Contact Information for Business Card

Balgo Groundworks Pty Ltd
ABN 58 402 917 364
82 Dunmore Creek Road, Narrabri NSW 2390

Desmond Fairweather
Managing Director
P 0438 614 205
E desfairweather@balgogroundworks.com.au

Font styles to use
Serif
Sans Serif

Requirements
Nice to have
• I have attached some examples of ideas.
Should not have
• images of machinery

```html
<!DOCTYPE html>
<html lang="en">
<head>
<meta charset="utf-8">
<title>Balgo Groundworks Business Card</title>
<link rel="stylesheet" href="https://fonts.googleapis.com/css2?family=Source+Sans+3:wght@400;700&display=swap">
<style>
  :root {
    --stage: #2a2a2a;
    --card-white: #ffffff;
    --card-charcoal: #444444;
    --brand-orange: #f08a1c;
    --ink: #3d3d3d;
    --rule: #8a8a8a;
    --on-dark: #ffffff;
  }
  * { margin: 0; padding: 0; box-sizing: border-box; }
  html, body { width: 1200px; height: 960px; overflow: hidden; }
  body {
    background: var(--stage);
    font-family: "Source Sans 3", "Myriad Pro", Arial, sans-serif;
    position: relative;
  }
  .card {
    position: absolute;
    left: 261px;
    width: 679px;
    height: 387px;
  }
  .card--front { top: 61px; background: var(--card-white); color: var(--ink); }
  .card--back { top: 511px; background: var(--card-charcoal); color: var(--on-dark); }

  .brand-name {
    font-weight: 700;
    text-transform: uppercase;
    line-height: 1.05;
    letter-spacing: 0.5px;
  }
  .card--front .brand-name {
    position: absolute;
    right: 44px;
    top: 46px;
    width: 300px;
    text-align: right;
    font-size: 34px;
    color: var(--brand-orange);
  }
  .card--back .brand-name {
    position: absolute;
    left: 0; right: 0;
    top: 130px;
    text-align: center;
    font-size: 46px;
    color: var(--on-dark);
  }

  .person { position: absolute; left: 37px; top: 215px; }
  .person__name {
    font-size: 25px;
    font-weight: 700;
    color: var(--brand-orange);
    text-transform: uppercase;
    line-height: 1;
  }
  .person__role { font-size: 18px; margin-top: 5px; margin-left: 3px; line-height: 1; }

  .divider {
    position: absolute;
    left: 36px; right: 36px;
    top: 275px;
    border-top: 1.5px solid var(--rule);
  }

  .contact-list {
    position: absolute;
    left: 36px; top: 288px;
    list-style: none;
    font-size: 17px;
  }
  .contact-list li { display: flex; align-items: center; height: 22.5px; }
  .contact-list svg { width: 15px; height: 15px; margin-right: 12px; fill: var(--brand-orange); flex: none; }

  .company-details {
    position: absolute;
    right: 44px; top: 288px;
    text-align: right;
    font-size: 17px;
    font-style: normal;
    line-height: 22.5px;
  }

  .specialties {
    position: absolute;
    left: 0; right: 0;
    top: 294px;
    text-align: center;
    font-size: 17px;
    line-height: 22px;
  }
</style>
</head>
<body>

<section class="card card--front" aria-label="Business card front">
  <div class="brand-name">Balgo Groundworks Pty Ltd</div>

  <div class="person">
    <p class="person__name">Desmond Fairweather</p>
    <p class="person__role">Managing Director</p>
  </div>

  <div class="divider"></div>

  <ul class="contact-list">
    <li>
      <svg viewBox="0 0 16 16" aria-hidden="true"><path d="M2 6c0-2 2-3.5 6-3.5S14 4 14 6v1h-3V5.5H5V7H2z"/><rect x="3" y="8" width="10" height="6" rx="1.5"/></svg>
      0438 614 205
    </li>
    <li>
      <svg viewBox="0 0 16 16" aria-hidden="true"><path d="M1 3h14v1.5L8 9 1 4.5z"/><path d="M1 6l7 4.5L15 6v7H1z"/></svg>
      desfairweather@balgogroundworks.com.au
    </li>
    <li>
      <svg viewBox="0 0 16 16" aria-hidden="true"><circle cx="8" cy="8" r="7"/><path d="M5 4.5l3 1-1 2.5-2 .5zM9.5 9l2.5-.5-.5 3-2 .5z" fill="#fff"/></svg>
      www.balgogroundworks.com.au
    </li>
  </ul>

  <address class="company-details">
    82 Dunmore Creek Road<br>
    Narrabri NSW 2390<br>
    ABN 58 402 917 364
  </address>
</section>

<section class="card card--back" aria-label="Business card back">
  <div class="brand-name">Balgo Groundworks<br>Pty Ltd</div>
  <p class="specialties">We specialise in<br>Agriculture, Civil Construction &amp; Mining.</p>
</section>

</body>
</html>
```